Two wall artworks for physiotherapy clinic waiting room

We are a physiotherapy clinic located in Glebe, Sydney. We have a clinic that is within a beautiful heritage listed building and we have two blank white walls that need artwork. Each artwork will be 3000mm wide and 1200mm high. Our clinic is mostly white and I will include our brand's colours below. We are looking for bright, beautiful artworks that are consistent with our colours. One of the artworks should include our full logo including the text so that customers see the name of the clinic on their way into the waiting room. I will include our logo in the files below, as well as images of the clinic, the walls and some other signs that we have already. We would prefer artworks with nice patterns or graphics rather than images of people.

```html
<!DOCTYPE html>
<html lang="en">
<head>
<meta charset="utf-8">
<title>Bayside Physio – Waiting Room Wall Artworks</title>
<link rel="stylesheet" href="https://fonts.googleapis.com/css2?family=Montserrat:wght@500;600&display=swap">
<style>
  :root {
    --navy: #2b2470;
    --teal: #3cc1b1;
    --teal-deep: #1fa9a6;
    --teal-light: #5fd0c1;
    --white: #ffffff;
    --page: #ffffff;
  }
  html, body {
    margin: 0;
    padding: 0;
    width: 1200px;
    height: 527px;
    overflow: hidden;
    background: var(--page);
  }
  .canvas {
    width: 1200px;
    height: 527px;
    display: flex;
    flex-direction: column;
    align-items: center;
    justify-content: center;
    gap: 18px;
  }
  .artwork {
    display: block;
    width: 600px;
    height: 240px;
    font-family: "Montserrat", sans-serif;
  }
  .brand-name {
    fill: var(--navy);
    font-weight: 600;
  }
  .brand-tagline {
    fill: var(--navy);
    font-weight: 500;
  }
  .service-label {
    fill: var(--navy);
    font-weight: 500;
    font-size: 7.5px;
  }
  .fill-navy { fill: var(--navy); }
  .fill-teal { fill: var(--teal); }
  .fill-teal-deep { fill: var(--teal-deep); }
  .fill-white { fill: var(--white); }
</style>
</head>
<body>
<main class="canvas">

  <!-- Wall one: wave panel, name and services -->
  <svg class="artwork artwork-services" viewBox="0 0 600 240" role="img" aria-label="Wall artwork with flowing teal and navy waves, clinic name and list of services">
    <defs>
      <linearGradient id="tealFlow" x1="0" y1="0" x2="1" y2="1">
        <stop offset="0" stop-color="var(--teal-light)"/>
        <stop offset="1" stop-color="var(--teal-deep)"/>
      </linearGradient>
    </defs>

    <g class="wave-panel">
      <path fill="url(#tealFlow)" d="M0 0 H306 C285 35 258 52 215 60 C150 72 80 62 40 95 C20 112 8 130 0 150 Z"/>
      <path class="fill-navy" d="M0 240 V185 C35 160 90 168 140 185 C190 202 240 200 270 215 C285 222 298 232 306 240 Z"/>
    </g>

    <g class="brand-lockup">
      <circle class="fill-teal" cx="342" cy="36" r="16"/>
      <text class="brand-name" x="366" y="45" font-size="25">Bayside Physio</text>
      <text class="brand-tagline" x="366" y="59" font-size="8.4">Physiotherapy and Exercise Physiology</text>
    </g>

    <g class="service-list">
      <circle class="fill-teal" cx="338" cy="95" r="17"/>
      <text class="service-label" x="364" y="98">Physiotherapy</text>

      <circle class="fill-navy" cx="338" cy="140" r="17"/>
      <text class="service-label" x="364" y="143">Exercise Physiology</text>

      <circle class="fill-teal" cx="338" cy="185" r="17"/>
      <text class="service-label" x="364" y="188">Pain Management</text>

      <circle class="fill-navy" cx="477" cy="98" r="17"/>
      <g class="icon-dumbbell" stroke="var(--white)" stroke-width="1.6" fill="none" stroke-linecap="round">
        <line x1="469" y1="98" x2="485" y2="98"/>
        <line x1="469" y1="92" x2="469" y2="104"/>
        <line x1="485" y1="92" x2="485" y2="104"/>
        <line x1="466" y1="95" x2="466" y2="101"/>
        <line x1="488" y1="95" x2="488" y2="101"/>
      </g>
      <text class="service-label" x="503" y="101">Strength &amp; Rehab</text>

      <circle class="fill-teal" cx="477" cy="142" r="17"/>
      <text class="service-label" x="503" y="145">Move Well Live Well</text>
    </g>

    <path class="fill-teal-deep corner-wave" d="M448 240 C468 226 495 216 518 204 C542 191 565 187 600 187 V240 Z"/>
  </svg>

  <!-- Wall two: centred name between waves -->
  <svg class="artwork artwork-welcome" viewBox="0 0 600 240" role="img" aria-label="Wall artwork with teal top wave, navy bottom hills and centred clinic name">
    <g class="top-wave">
      <path class="fill-teal-deep" d="M0 0 H600 V20 C590 50 575 70 545 66 C515 62 495 48 470 62 C445 76 410 80 385 66 C360 52 330 70 300 76 C270 82 250 62 225 62 C195 62 180 82 150 78 C120 74 110 55 85 56 C55 57 40 80 20 74 C8 70 3 40 0 22 Z"/>
      <path class="fill-teal" d="M0 0 H600 V14 C588 40 572 58 545 56 C515 54 495 40 470 52 C445 64 412 68 387 56 C362 44 332 60 300 66 C270 72 250 52 225 52 C195 52 180 70 150 66 C120 62 110 45 85 46 C55 47 40 68 20 62 C8 58 3 30 0 14 Z"/>
    </g>

    <g class="brand-lockup">
      <circle class="fill-teal" cx="140" cy="112" r="30"/>
      <text class="brand-name" x="224" y="126" font-size="41">Bayside Physio</text>
      <text class="brand-tagline" x="226" y="150" font-size="14.6">Physiotherapy and Exercise Physiology</text>
    </g>

    <path class="fill-navy bottom-hills" d="M0 240 V225 C10 195 35 178 70 180 C105 182 130 200 165 205 C200 210 225 195 255 178 C280 164 300 162 325 172 C350 182 365 196 390 190 C415 184 430 168 455 168 C480 168 495 182 520 180 C550 178 575 175 590 195 C597 205 600 220 600 240 Z"/>
  </svg>

</main>
</body>
</html>
```